Design for a 4 screens iOS and Android app - "TrajiMesur"

The app allows you to track your car gasoline refill ...
We need a design for the 4 screens of the app:
a) 1 form with 3 fields.
b) 1 simple list view
c) 1 summary view
d) 1 text page
2 "alerts" items are also to be designed.
No specific guidelines, nor logo or whatever.
It will be a free app distributed on iOS and Androïd.
We just want to make it looking nice & very usable for end users.
Target Market(s)
B2C app
Industry/Entity Type
Android

```html
<!DOCTYPE html>
<html lang="en">
<head>
<meta charset="utf-8">
<title>TrajiMesur – Add Receipt</title>
<link rel="stylesheet" href="https://fonts.googleapis.com/css2?family=Mulish:wght@400;600;700;800&display=swap">
<style>
  :root {
    --page-bg: #e9e9e9;
    --bar-dark: #2a2a2a;
    --bar-text: #ffffff;
    --tab-bg: #f3f3f3;
    --tab-active: #ffffff;
    --tab-line: #d9d9d9;
    --tab-icon: #9a9a9a;
    --ink: #2b2b2b;
    --form-bg: #f8f8f8;
    --field-bg: #eaeaea;
    --field-text: #555555;
    --unit-text: #a8a8a8;
    --error: #e8322f;
    --save: #4ad865;
  }
  * { box-sizing: border-box; margin: 0; padding: 0; }
  html, body {
    width: 1200px; height: 1139px; overflow: hidden;
    background: var(--page-bg);
    font-family: "Mulish", "Helvetica Neue", Arial, sans-serif;
  }
  .screen {
    position: absolute; left: 319px; top: 70px;
    width: 562px; height: 1000px;
    background: var(--form-bg);
    box-shadow: 0 10px 40px rgba(0,0,0,0.12);
    overflow: hidden;
  }
  .status-bar {
    height: 30px; background: var(--bar-dark); color: var(--bar-text);
    display: flex; align-items: center; justify-content: space-between;
    padding: 0 10px; font-size: 16px; font-weight: 600; position: relative;
  }
  .status-left, .status-right { display: flex; align-items: center; gap: 6px; }
  .status-time { position: absolute; left: 50%; transform: translateX(-50%); }
  .nav-bar {
    height: 66px; background: var(--bar-dark); color: var(--bar-text);
    display: flex; align-items: center; justify-content: center; position: relative;
  }
  .nav-title { font-size: 25px; font-weight: 800; }
  .nav-action { position: absolute; right: 18px; font-size: 24px; font-weight: 400; }
  .tab-bar {
    height: 74px; background: var(--tab-bg); display: flex;
    border-bottom: 1px solid var(--tab-line);
  }
  .tab {
    flex: 1; display: flex; align-items: center; justify-content: center;
    border-left: 1px solid var(--tab-line);
  }
  .tab:first-child { border-left: none; }
  .tab.is-active { background: var(--tab-active); border-bottom: 3px solid var(--ink); }
  .receipt-form { padding: 22px 24px; }
  .field { margin-bottom: 20px; }
  .field-label { display: block; font-size: 24px; font-weight: 800; color: var(--ink); margin-bottom: 10px; }
  .field-input {
    height: 56px; background: var(--field-bg); border-radius: 7px;
    border: 1px solid transparent;
    display: flex; align-items: center; justify-content: space-between;
    padding: 0 22px; font-size: 25px; color: var(--field-text);
  }
  .field-input.has-error { border-color: var(--error); background: #f2f2f2; }
  .field-unit { color: var(--unit-text); font-size: 22px; }
  .save-button {
    margin-top: 14px; width: 100%; height: 76px; border: none; border-radius: 7px;
    background: var(--save); color: #fff; font-family: inherit;
    font-size: 30px; font-weight: 800;
  }
</style>
</head>
<body>
  <main class="screen">
    <div class="status-bar">
      <div class="status-left">
        <span>●●●●●</span><span>CARRIER</span>
        <svg width="18" height="14" viewBox="0 0 18 14"><path d="M1 5a12 12 0 0 1 16 0M4 8a7.5 7.5 0 0 1 10 0M7 11a3 3 0 0 1 4 0" stroke="#fff" stroke-width="2" fill="none"/></svg>
      </div>
      <span class="status-time">4:21 PM</span>
      <div class="status-right">
        <svg width="10" height="16" viewBox="0 0 10 16"><path d="M1 4l8 8-4 3V1l4 3-8 8" stroke="#fff" stroke-width="1.5" fill="none"/></svg>
        <span>22%</span>
        <svg width="34" height="16" viewBox="0 0 34 16"><rect x="1" y="1" width="28" height="14" rx="3" stroke="#fff" stroke-width="1.5" fill="none"/><rect x="3" y="3" width="6" height="10" fill="#fff"/><rect x="30" y="5" width="3" height="6" fill="#fff"/></svg>
      </div>
    </div>
    <header class="nav-bar">
      <h1 class="nav-title">Add Receipt</h1>
      <span class="nav-action">About</span>
    </header>
    <nav class="tab-bar">
      <div class="tab is-active">
        <svg width="36" height="36" viewBox="0 0 36 36"><path d="M18 3v30M3 18h30" stroke="#2b2b2b" stroke-width="3.5"/></svg>
      </div>
      <div class="tab">
        <svg width="44" height="34" viewBox="0 0 44 34" fill="#9a9a9a"><circle cx="4" cy="4" r="3"/><circle cx="4" cy="17" r="3"/><circle cx="4" cy="30" r="3"/><rect x="12" y="2" width="32" height="4"/><rect x="12" y="15" width="32" height="4"/><rect x="12" y="28" width="32" height="4"/></svg>
      </div>
      <div class="tab">
        <svg width="34" height="34" viewBox="0 0 34 34" fill="#9a9a9a"><rect x="2" y="22" width="6" height="10"/><rect x="11" y="16" width="6" height="16"/><rect x="20" y="10" width="6" height="22"/><path d="M26 2l6 6h-4v24h-4V8h-4z"/></svg>
      </div>
    </nav>
    <form class="receipt-form">
      <div class="field">
        <label class="field-label">Kilometer Count</label>
        <div class="field-input"><span>127500</span><span class="field-unit">km</span></div>
      </div>
      <div class="field">
        <label class="field-label">Litre</label>
        <div class="field-input has-error"><span>qqqqqq</span><span class="field-unit">L</span></div>
      </div>
      <div class="field">
        <label class="field-label">Price</label>
        <div class="field-input"><span></span><span class="field-unit">€</span></div>
      </div>
      <button class="save-button" type="button">Save</button>
    </form>
  </main>
</body>
</html>
```